Property developer, money partner needs business card design using logo concept provided

Our company develops residential properties, does money lends for joint ventures in property deals and finds property deals for other money partners. We have provided a basic logo for you to work from. Any graphic or logo design on the card is to communicate development and finance collaboration. Color choice is not so important for us, but color choice does need to reflect professionalism.

```html
<!DOCTYPE html>
<html lang="en">
<head>
<meta charset="utf-8">
<title>Hearthline Property Solutions – Business Card</title>
<link href="https://fonts.googleapis.com/css2?family=Montserrat:wght@400;500;600&display=swap" rel="stylesheet">
<style>
  :root {
    --page-bg: #eef2f6;
    --card-white: #ffffff;
    --brand-blue: #0a4f9c;
    --brand-red: #a3161c;
    --ink: #1d1d1f;
    --on-blue: #ffffff;
  }
  * { margin: 0; padding: 0; box-sizing: border-box; }
  html, body {
    width: 1200px; height: 1200px; overflow: hidden;
    background: var(--page-bg);
    font-family: "Montserrat", Arial, sans-serif;
  }
  .canvas { position: relative; width: 1200px; height: 1200px; }

  .card {
    position: absolute; left: 164px; width: 871px; height: 513px;
    background: var(--card-white); overflow: hidden;
  }
  .card--front { top: 75px; }
  .card--back { top: 618px; }
  .card-shapes { position: absolute; inset: 0; width: 100%; height: 100%; }
  .shape-blue { fill: var(--brand-blue); }
  .shape-red { fill: var(--brand-red); }

  .brand { position: absolute; text-align: center; transform: translateX(-50%); color: var(--ink); }
  .brand-disc { display: block; margin: 0 auto; border-radius: 50%; background: var(--brand-blue); }
  .brand-name { font-weight: 600; letter-spacing: 0.14em; line-height: 1.1; white-space: nowrap; }
  .brand-acn { font-weight: 500; letter-spacing: 0.08em; }

  .card--front .brand { left: 201px; top: 56px; }
  .card--front .brand-disc { width: 200px; height: 200px; margin-bottom: 26px; }
  .card--front .brand-name { font-size: 22px; }
  .card--front .brand-acn { font-size: 11px; margin-top: 4px; }

  .card--back .brand { left: 436px; top: 112px; }
  .card--back .brand-disc { width: 240px; height: 240px; margin-bottom: 32px; }
  .card--back .brand-name { font-size: 29px; }
  .card--back .brand-acn { font-size: 13px; margin-top: 5px; }

  .person { position: absolute; right: 76px; top: 98px; text-align: right; color: var(--on-blue); }
  .person-name { font-size: 28px; font-weight: 500; letter-spacing: 0.04em; line-height: 1.12; text-transform: uppercase; }
  .person-title { font-size: 22px; font-weight: 400; margin-top: 2px; }
  .divider { position: absolute; left: 579px; top: 248px; width: 216px; height: 3px; background: var(--on-blue); }

  .contact-list { list-style: none; }
  .contact-item {
    position: absolute; right: 76px; height: 28px;
    display: flex; align-items: center; gap: 14px;
    color: var(--on-blue); font-size: 20px; font-weight: 400; white-space: nowrap;
  }
  .contact-item svg { width: 20px; height: 20px; fill: none; stroke: var(--on-blue); stroke-width: 1.8; }
  .contact-phone { top: 297px; }
  .contact-email { top: 331px; }
  .contact-web { top: 364px; }
  .contact-address { top: 424px; }
</style>
</head>
<body>
<main class="canvas">

  <section class="card card--front" aria-label="Business card front">
    <svg class="card-shapes" viewBox="0 0 697 410" preserveAspectRatio="none" aria-hidden="true">
      <polygon class="shape-red" points="289,0 301,0 301,250 228,345 305,410 292,410 212,342 289,244"/>
      <polygon class="shape-blue" points="301,0 697,0 697,410 305,410 228,345 301,250"/>
    </svg>

    <div class="brand">
      <span class="brand-disc"></span>
      <p class="brand-name">HEARTHLINE</p>
      <p class="brand-name">Property Solutions</p>
      <p class="brand-acn">A.C.N 618 204 337</p>
    </div>

    <div class="person">
      <p class="person-name">Daniel<br>Whitmore</p>
      <p class="person-title">CEO, President</p>
    </div>
    <div class="divider"></div>

    <ul class="contact-list">
      <li class="contact-item contact-phone">1300 555 019
        <svg viewBox="0 0 24 24"><path d="M5 3h4l2 5-2.5 1.5a11 11 0 0 0 6 6L16 13l5 2v4a2 2 0 0 1-2 2A16 16 0 0 1 3 5a2 2 0 0 1 2-2z"/></svg>
      </li>
      <li class="contact-item contact-email">info@hearthline.com.au
        <svg viewBox="0 0 24 24"><rect x="3" y="5" width="18" height="14"/><path d="M3 5l9 8 9-8"/></svg>
      </li>
      <li class="contact-item contact-web">www.hearthline.com.au
        <svg viewBox="0 0 24 24"><circle cx="12" cy="12" r="9"/><path d="M3 12h18M12 3c3 3 3 15 0 18M12 3c-3 3-3 15 0 18"/></svg>
      </li>
      <li class="contact-item contact-address">48 Ridgeview Rd Maleny Q 4552
        <svg viewBox="0 0 24 24"><path d="M12 21s-6-6.5-6-11a6 6 0 0 1 12 0c0 4.5-6 11-6 11z"/><circle cx="12" cy="10" r="2.2"/></svg>
      </li>
    </ul>
  </section>

  <section class="card card--back" aria-label="Business card back">
    <svg class="card-shapes" viewBox="0 0 697 410" preserveAspectRatio="none" aria-hidden="true">
      <polygon class="shape-red" points="108,0 122,0 199,62 126,152 126,410 114,410 114,150 185,62"/>
      <polygon class="shape-blue" points="0,0 108,0 185,62 114,150 114,410 0,410"/>
    </svg>

    <div class="brand">
      <span class="brand-disc"></span>
      <p class="brand-name">HEARTHLINE</p>
      <p class="brand-name">Property Solutions</p>
      <p class="brand-acn">A.C.N 618 204 337</p>
    </div>
  </section>

</main>
</body>
</html>
```